Poster & Banner for Outback tour company

Poster needed for tour company in the Australian outback. We will need it in an A2 format and if possible a larger banner format as Well please. It needs the Kestrel Tours logo but also the other logos (less obvious). It also needs to feature the Vantorix logo (uploaded).

The poster needs a list of the tours we offer as well as some of the pictures uploaded.

List of tours:

- Deluxe Tour of the Village and the Redspurs $99
- Marrandi Scenic Tour $85
- Starlight Redspurs Tour $60
- Quartz Trailside Tour $50

Industry/Entity Type

Tour Company

Font styles to use
Serif

Colors

Designer to choose colors to be used in the design.

Requirements
Must have
• Kestrel Tours logo/List of tours/

```html
<!DOCTYPE html>
<html lang="en">
<head>
<meta charset="utf-8">
<title>Kestrel Tours – Outback Tours Poster</title>
<link href="https://fonts.googleapis.com/css2?family=Open+Sans:wght@700;800&family=Questrial&display=swap" rel="stylesheet">
<style>
  :root {
    --stage: #e9e6e2;
    --cream: #fcebd8;
    --brown-dark: #3a2314;
    --ochre: #c47a1b;
    --teal: #3b7a8c;
    --red: #b5121b;
    --white: #ffffff;
    --badge-green: #34e0a1;
    --sky-top: #8fb0d8;
    --sky-low: #d8d2c6;
    --rock: #a86a48;
    --sand: #b98262;
  }
  * { margin: 0; padding: 0; box-sizing: border-box; }
  html, body { width: 900px; height: 1200px; overflow: hidden; background: var(--stage); }
  .poster {
    position: absolute; left: 25px; top: 0;
    width: 850px; height: 1200px; overflow: hidden;
    background: var(--cream);
    font-family: "Questrial", sans-serif;
    color: var(--brown-dark);
  }
  .backdrop { position: absolute; inset: 0; }
  .hero-photo {
    position: absolute; left: 0; top: 0; width: 850px; height: 780px;
    background:
      linear-gradient(90deg, rgba(150,80,50,.85) 0, rgba(150,80,50,0) 18%, rgba(150,80,50,0) 82%, rgba(140,75,45,.85) 100%),
      linear-gradient(180deg, var(--sky-top) 0%, var(--sky-low) 40%, var(--rock) 58%, var(--sand) 80%, #9d6446 100%);
  }
  .brand { position: absolute; top: 60px; left: 0; width: 850px; text-align: center; }
  .brand-mark {
    display: inline-block; width: 58px; height: 58px;
    background: var(--ochre); border-radius: 6px; margin-bottom: 18px;
  }
  .brand-name {
    font-family: "Open Sans", sans-serif; font-weight: 800;
    font-size: 54px; letter-spacing: -1px; color: var(--brown-dark); line-height: 1;
  }
  .tours { position: absolute; top: 464px; left: 43px; }
  .tour-card {
    position: absolute; top: 0; width: 185px; height: 377px;
    background: var(--white); border-radius: 93px;
    box-shadow: 0 3px 8px rgba(0,0,0,.18);
    text-align: center; overflow: hidden;
  }
  .tour-photo {
    width: 163px; height: 163px; border-radius: 50%;
    margin: 12px auto 0;
  }
  .tour-title {
    margin-top: 16px; font-size: 21px; line-height: 24px; padding: 0 6px;
  }
  .tour-price {
    position: absolute; left: 17px; bottom: 0; width: 151px; height: 76px;
    border-radius: 50%;
    font-family: "Open Sans", sans-serif; font-weight: 700;
    font-size: 40px; line-height: 76px; color: var(--white);
  }
  .price-ochre { background: var(--ochre); }
  .price-teal { background: var(--teal); }
  .price-brown { background: var(--brown-dark); }
  .price-red { background: var(--red); }
  .photo-church { background: radial-gradient(circle at 50% 55%, #b3582b, #5a2a17 75%); }
  .photo-dugout { background: linear-gradient(180deg, #d07a2d 0%, #8a5634 55%, #5e4537 100%); }
  .photo-sunset { background: linear-gradient(180deg, #1d2a55 0%, #3b4f83 45%, #e08a3c 78%, #1a130e 86%); }
  .photo-tunnel { background: radial-gradient(circle at 40% 45%, #9fa6a2, #4b4a45 70%); }

  .booking { position: absolute; left: 134px; top: 902px; width: 580px; height: 78px; }
  .booking-frame {
    position: absolute; inset: 0; border: 1.5px solid var(--ochre); border-radius: 10px;
  }
  .booking-head {
    position: absolute; top: -26px; left: 0; width: 100%;
    display: flex; justify-content: center; align-items: center;
  }
  .booking-head-inner {
    display: flex; align-items: center; gap: 14px;
    background: var(--cream); padding: 0 14px;
  }
  .booking-icon { width: 54px; height: 54px; }
  .booking-label { font-size: 35px; line-height: 1; }
  .booking-url {
    position: absolute; top: 34px; left: 0; width: 100%; text-align: center;
    font-family: "Open Sans", sans-serif; font-weight: 800; font-size: 33px;
    letter-spacing: -1.4px; line-height: 1;
  }

  .partners {
    position: absolute; top: 1020px; left: 214px; height: 52px;
    display: flex; align-items: center;
  }
  .partner { font-size: 16px; color: var(--brown-dark); padding: 0 14px; display: flex; align-items: center; gap: 6px; }
  .partner-dot { width: 12px; height: 12px; background: var(--ochre); border-radius: 50%; }
  .partner-divider { width: 1.5px; height: 50px; background: var(--brown-dark); }

  .award-badge {
    position: absolute; left: 727px; top: 1069px; width: 96px; height: 114px;
    background: var(--badge-green);
  }

  .footer { position: absolute; left: 0; top: 1112px; width: 850px; height: 88px; }
  .footer-shapes { position: absolute; inset: 0; }
  .contact-main { position: absolute; left: 55px; top: 16px; color: var(--white); }
  .contact-lead { font-size: 17px; }
  .contact-phone {
    display: flex; align-items: center; gap: 10px; margin-top: 4px;
    font-family: "Open Sans", sans-serif; font-weight: 700; font-size: 27px; line-height: 1;
  }
  .contact-details { position: absolute; left: 424px; top: 29px; color: var(--white); }
  .contact-line { display: flex; align-items: center; gap: 8px; }
  .contact-email { font-size: 16px; }
  .contact-address { font-size: 10px; margin-top: 6px; }
</style>
</head>
<body>
<main class="poster">
  <div class="hero-photo" role="img" aria-label="Photograph of a tour truck parked in a red desert canyon with mesas under a clear sky"></div>

  <svg class="backdrop" width="850" height="1200" viewBox="0 0 850 1200" aria-hidden="true">
    <path d="M0,705 C320,690 640,640 850,470 L850,505 C640,675 320,725 0,740 Z" fill="var(--brown-dark)"/>
    <path d="M560,620 C680,570 780,500 850,430 L850,470 C760,540 660,610 540,650 Z" fill="var(--ochre)"/>
    <path d="M0,740 C320,725 640,675 850,505 L850,1200 L0,1200 Z" fill="var(--cream)"/>
  </svg>

  <header class="brand">
    <span class="brand-mark"></span>
    <h1 class="brand-name">KESTREL TOURS</h1>
  </header>

  <section class="tours">
    <article class="tour-card" style="left:0">
      <div class="tour-photo photo-church" role="img" aria-label="Photograph of an underground church interior with stained glass"></div>
      <h2 class="tour-title">Deluxe Tour<br>of the Village<br>and the<br>Redspurs</h2>
      <div class="tour-price price-ochre">$99</div>
    </article>
    <article class="tour-card" style="left:193px">
      <div class="tour-photo photo-dugout" role="img" aria-label="Photograph of cave dugouts in an orange cliff with a tour bus"></div>
      <h2 class="tour-title">Marrandi<br>Scenic<br>Tour</h2>
      <div class="tour-price price-teal">$85</div>
    </article>
    <article class="tour-card" style="left:385px">
      <div class="tour-photo photo-sunset" role="img" aria-label="Photograph of a mining machine silhouetted against a sunset sky"></div>
      <h2 class="tour-title">Starlight<br>Redspurs<br>Tour</h2>
      <div class="tour-price price-brown">$60</div>
    </article>
    <article class="tour-card" style="left:578px">
      <div class="tour-photo photo-tunnel" role="img" aria-label="Photograph of a visitor exploring an underground mine tunnel"></div>
      <h2 class="tour-title">Quartz<br>Trailside<br>Tour</h2>
      <div class="tour-price price-red">$50</div>
    </article>
  </section>

  <section class="booking">
    <div class="booking-frame"></div>
    <div class="booking-head">
      <div class="booking-head-inner">
        <svg class="booking-icon" viewBox="0 0 54 54" aria-hidden="true">
          <circle cx="27" cy="27" r="25" fill="var(--white)" stroke="var(--ochre)" stroke-width="2"/>
          <path d="M21,15 L21,38 L27,32 L31,41 L35,39 L31,30 L39,30 Z" fill="none" stroke="var(--ochre)" stroke-width="2.2" stroke-linejoin="round"/>
        </svg>
        <span class="booking-label">Online bookings</span>
      </div>
    </div>
    <p class="booking-url">www.kestreltoursaustralia.com.au</p>
  </section>

  <section class="partners">
    <span class="partner"><span class="partner-dot"></span>Dunmore Ridge</span>
    <span class="partner-divider"></span>
    <span class="partner">Parkhaven</span>
    <span class="partner-divider"></span>
    <span class="partner">Willowmere</span>
    <span class="partner-divider"></span>
    <span class="partner">Claystone Motel</span>
  </section>

  <div class="award-badge" role="img" aria-label="Vantorix award badge"></div>

  <footer class="footer">
    <svg class="footer-shapes" width="850" height="88" viewBox="0 0 850 88" aria-hidden="true">
      <rect x="0" y="22" width="850" height="47" fill="var(--ochre)"/>
      <path d="M0,0 L350,0 C372,0 380,10 386,22 L406,88 L0,88 Z" fill="var(--brown-dark)"/>
    </svg>
    <div class="contact-main">
      <p class="contact-lead">Contact us for more information!</p>
      <p class="contact-phone">
        <svg width="24" height="24" viewBox="0 0 24 24" aria-hidden="true">
          <path d="M6.5,2.5 L9.5,6.5 L7.5,9 C8.8,11.8 11.2,14.2 14.5,16 L17,14 L21,17 L19,21 C11,21 3,13 3,5 Z" fill="none" stroke="var(--white)" stroke-width="2" stroke-linejoin="round"/>
        </svg>
        +61 400 555 018
      </p>
    </div>
    <div class="contact-details">
      <p class="contact-line contact-email">
        <svg width="16" height="12" viewBox="0 0 16 12" aria-hidden="true">
          <rect x="0.5" y="0.5" width="15" height="11" fill="var(--white)"/>
          <path d="M0.5,0.5 L8,7 L15.5,0.5" fill="none" stroke="var(--ochre)" stroke-width="1.2"/>
        </svg>
        hello@kestreltoursmail.com
      </p>
      <p class="contact-line contact-address">
        <svg width="12" height="15" viewBox="0 0 12 15" aria-hidden="true">
          <path d="M6,14.5 C2,9 0.8,7 0.8,5.3 A5.2,5.2 0 0 1 11.2,5.3 C11.2,7 10,9 6,14.5 Z" fill="var(--white)"/>
          <circle cx="6" cy="5.3" r="2" fill="var(--ochre)"/>
        </svg>
        Kestrel Tours PO Box 210, Marrandi 5999, SA
      </p>
    </div>
  </footer>
</main>
</body>
</html>
```